Web Design Project for a new website

We need a web design for a new proposed social media site ,intially to judge market response, this would be a basic site 4 pages with a register page for visitors to register with email and possibly start their own profile page with a template that would be on the site.
the domain is zenthra.net with the tagline dream climb reach zenthra ,,it has 2 aa in zenthra ,the main function and the message we would like to convey is that if you aspire to achieve your goals,aim in life ,change your life ,the site will recognize and reward you with a status rank more like a life rank,example is brivane 1000 most influential people,this would allow you to network with other likeminded people who register on site and progress of your goal could be monitored via your profile page.
There are 4 categories of how to become world zenthra
Star,Hero,Leader,Icon
And one category Q-7 which is a open forum on the science of success to which people registered can contribute and source info.
The design has to communicate the message of the site in a proffessional modern way with distinct colours and and logo that can be visually striking .

deadline is friday the 5th please submit your designs

Please submit designs as last day of deadline 5th august.

Reason: some designers have asked for extra time so obliging but cant extend any further so please submit designs by deadline .

Reason: 1 designer has asked for days extension.

12 to 80 all levels

Media

• see attached file for logo and design of zenthra the file can be changed or formatted or if be your own individual design on the same theme ,the main web logo of zenthra would also be the logo with a different colour identity fo categories STAR,HERO,LEADER,ICON ,Q-7
• zenthra.net should have the tagline dream,climb,reach zenthra
zenthra.net
dream,climb,reach zenthra,
the logo should indicate being world zenthra,a globe as per file image.some background messages like aspire,achive,be a world leader,can be used as background.

```html
<!DOCTYPE html>
<html lang="en">
<head>
<meta charset="utf-8">
<title>zenthra.net – Register</title>
<link href="https://fonts.googleapis.com/css2?family=Arimo:wght@400;700&display=swap" rel="stylesheet">
<style>
:root{
  --bg-top:#c9dbe1;
  --bg-bottom:#e4edf0;
  --ink:#4d4f5c;
  --link-blue:#4a6a8a;
  --purple:#8c5ca8;
  --nav-top:#7d98ad;
  --nav-bottom:#b9c6ce;
  --ribbon:#d9d6c6;
  --panel:#566580;
  --panel-edge:#9aa6b5;
  --field-top:#ffffff;
  --field-bottom:#ddd9c3;
  --info-bg:#c6d6df;
  --info-head-top:#88a2b8;
  --info-head-bottom:#5f7f9a;
  --card:#c6c9cf;
  --star:#f0801a;
  --hero:#2a66a6;
  --leader:#5f8f2a;
  --icon:#c8276e;
  --win-red:#e3341c;
  --rule:#9fb8c2;
}
*{box-sizing:border-box;margin:0;padding:0}
html,body{width:1200px;height:740px;overflow:hidden}
body{
  position:relative;
  font-family:"Arimo",Arial,sans-serif;
  color:var(--ink);
  background:linear-gradient(180deg,var(--bg-top) 0%,var(--bg-bottom) 45%,#dde8ec 100%);
}
.abs{position:absolute}

/* header */
.brand{left:120px;top:43px;width:308px;height:79px;border-radius:8px;
  background:linear-gradient(#f7f7fa,#e2e3ea);box-shadow:0 0 8px rgba(60,80,110,.35);
  display:flex;align-items:center;gap:12px;padding-left:18px}
.brand-dot{width:46px;height:46px;border-radius:50%;background:var(--purple);flex:none}
.brand-name{font-size:30px;font-weight:700;color:var(--purple);line-height:1}
.brand-tag{font-size:12px;color:var(--purple);margin-top:4px}
.login-label{left:449px;top:72px;font-size:12px}
.field-top{top:64px;height:29px;border:1px solid #c9c3a4;border-radius:4px;
  background:linear-gradient(var(--field-top),var(--field-bottom));
  font-size:11px;color:#a8a694;padding:8px 14px}
.join{left:846px;top:64px;width:71px;height:29px;border-radius:4px;border:1px solid #b3b3bd;
  background:linear-gradient(#e8e8ee,#c4c4cd);font-size:12px;text-align:center;line-height:27px}
.forgot{left:564px;top:104px;font-size:11px;color:var(--link-blue)}
.remember{left:673px;top:104px;font-size:11px;color:var(--link-blue);display:flex;gap:7px;align-items:center}
.check{width:11px;height:11px;border:1px solid #9aa;border-radius:2px;background:#fff}
.slogan{left:937px;top:62px;font-size:14px;color:var(--purple);line-height:17px}

/* navigation */
.ribbon{left:107px;top:152px;width:986px;height:36px}
.nav{left:137px;top:150px;width:928px;height:40px;border-radius:3px;
  background:linear-gradient(var(--nav-top),var(--nav-bottom));
  box-shadow:0 2px 4px rgba(40,60,80,.3);display:flex;align-items:center}
.nav-item{height:40px;line-height:40px;color:#fff;font-size:14px;padding:0 26px;
  border-right:1px solid rgba(255,255,255,.25)}
.nav-item.current{background:rgba(60,90,120,.25)}
.nav-home{width:72px;display:flex;align-items:center;justify-content:center}
.search{left:762px;top:156px;width:292px;height:29px;display:flex;border-radius:4px;overflow:hidden;
  box-shadow:0 1px 2px rgba(0,0,0,.2)}
.search-adv{width:76px;background:linear-gradient(#d9e6ea,#b6cbd3);font-size:12px;color:#3f5f7a;
  display:flex;align-items:center;justify-content:center;gap:3px}
.search-input{flex:1;background:linear-gradient(#fff,#e4e0cc);font-size:12px;padding:0 16px;
  display:flex;align-items:center;justify-content:space-between;color:#555}

/* register form */
.register{left:160px;top:225px;width:201px;height:338px;background:var(--panel);
  border:2px solid var(--panel-edge);border-radius:5px}
.register-tab{left:210px;top:218px;width:93px;height:34px;border-radius:0 0 8px 8px;
  background:linear-gradient(#7b96a3,#4f6c7b);color:#fff;font-size:12px;text-align:center;line-height:34px;
  box-shadow:0 2px 3px rgba(0,0,0,.3)}
.form-label{left:181px;font-size:11px;color:#fff}
.form-field{left:176px;width:169px;height:27px;border-radius:3px;
  background:linear-gradient(var(--field-top),var(--field-bottom))}
.agree{left:177px;top:501px;font-size:11px;color:#fff;display:flex;gap:8px;align-items:center}
.agree .check{background:#dfe4ea}
.signup{left:222px;top:524px;width:71px;height:27px;border-radius:4px;border:1px solid #9aa;
  background:linear-gradient(#eef0f6,#b8bfcc);font-size:11px;color:#2f4f7a;text-align:center;line-height:25px}

/* registration info */
.info{left:385px;top:245px;width:171px;height:302px;background:var(--info-bg);border-radius:4px;overflow:hidden}
.info-head{height:39px;background:linear-gradient(var(--info-head-top),var(--info-head-bottom));
  color:#fff;font-size:16px;text-align:center;line-height:40px}
.info-body{padding:14px 6px 0 9px;font-size:12px;line-height:14.3px;color:#4e5566}
.info-body p+p{margin-top:14px}

/* categories */
.cards{left:578px;width:470px;height:125px}
.badge{width:68px;height:68px;border-radius:50%;border:3px solid #fff;box-shadow:0 1px 3px rgba(0,0,0,.35)}
.cat-title{font-size:20px;font-weight:700}
.cat-text{font-size:12px;line-height:14.5px;color:#4e5566;width:200px}
.more{font-weight:700;font-size:11px;color:#555;text-decoration:underline;margin-left:10px}

/* footer */
.rule{left:137px;width:946px;height:1px;background:linear-gradient(90deg,transparent,var(--rule) 15%,var(--rule) 85%,transparent)}
.win-badge{left:240px;top:607px;width:68px;height:68px;border-radius:50%;border:3px solid #fff;
  background:radial-gradient(circle,#f4a21c,#e0401b);box-shadow:0 1px 3px rgba(0,0,0,.35)}
.win-title{left:328px;top:607px;font-size:21px;font-weight:700;color:var(--win-red)}
.win-text{left:329px;top:632px;width:380px;font-size:12px;line-height:14.5px;color:#4e5566}
.social{width:28px;height:28px;border-radius:50%;border:2px solid #fff;box-shadow:0 1px 2px rgba(0,0,0,.3)}
.foot-links{left:879px;top:616px;font-size:11px;line-height:14px;color:var(--link-blue);list-style:none}
.copyright{left:859px;top:699px;font-size:10px;color:#6a7a88}
</style>
</head>
<body>

<!-- header -->
<div class="abs brand">
  <span class="brand-dot"></span>
  <div>
    <div class="brand-name">zenthra.net</div>
    <div class="brand-tag">dream, climb, reach zenthra</div>
  </div>
</div>
<span class="abs login-label">Login</span>
<div class="abs field-top" style="left:485px;width:171px">Username</div>
<div class="abs field-top" style="left:664px;width:171px">Password</div>
<div class="abs join">Join</div>
<span class="abs forgot">Forget password</span>
<span class="abs remember"><span class="check"></span>Remember</span>
<p class="abs slogan">World's largest website<br>for zenthra people</p>

<!-- navigation -->
<svg class="abs ribbon" viewBox="0 0 986 36" aria-hidden="true">
  <polygon points="0,0 40,0 40,36 0,36 14,18" fill="var(--ribbon)"/>
  <polygon points="986,0 946,0 946,36 986,36 972,18" fill="var(--ribbon)"/>
  <polygon points="0,0 30,-2 30,34 0,36 12,18" fill="#9fb3c2"/>
  <polygon points="986,0 956,-2 956,34 986,36 974,18" fill="#9fb3c2"/>
</svg>
<nav class="abs nav">
  <div class="nav-item nav-home">
    <svg width="26" height="22" viewBox="0 0 26 22" aria-label="Home"><path d="M13 1 L25 12 H21 V21 H15 V15 H11 V21 H5 V12 H1 Z" fill="#fff"/></svg>
  </div>
  <div class="nav-item">About Us</div>
  <div class="nav-item">My Profile</div>
  <div class="nav-item">Q-7</div>
  <div class="nav-item current">Register</div>
  <div class="nav-item" style="border-right:none">Contact Us</div>
</nav>
<div class="abs search">
  <div class="search-adv">Advanced <svg width="8" height="5" viewBox="0 0 8 5"><path d="M0 0 H8 L4 5Z" fill="#3f5f7a"/></svg></div>
  <div class="search-input">Search
    <svg width="16" height="16" viewBox="0 0 16 16" aria-hidden="true"><circle cx="6.5" cy="6.5" r="5" fill="none" stroke="#888" stroke-width="2"/><path d="M10 10 L15 15" stroke="#888" stroke-width="2.5"/></svg>
  </div>
</div>

<!-- register form -->
<div class="abs register"></div>
<div class="abs register-tab">Register</div>
<span class="abs form-label" style="top:256px">Name*</span>
<div class="abs form-field" style="top:271px"></div>
<span class="abs form-label" style="top:304px">Surname</span>
<div class="abs form-field" style="top:319px"></div>
<span class="abs form-label" style="top:353px">Email*</span>
<div class="abs form-field" style="top:368px"></div>
<span class="abs form-label" style="top:402px">Password*</span>
<div class="abs form-field" style="top:417px"></div>
<span class="abs form-label" style="top:450px">Retype Password*</span>
<div class="abs form-field" style="top:465px"></div>
<span class="abs agree"><span class="check"></span>I agree the Terms &amp; Conditions</span>
<div class="abs signup">Sign up</div>

<!-- registration info -->
<section class="abs info">
  <h2 class="info-head" style="font-weight:400">Registration Info</h2>
  <div class="info-body">
    <p>Lorem ipsum dolor sit amet, consectetur adipisicing elit, sed do eiusmod tempor incididunt ut labore et dolore magna aliqua. Ut enim ad minim veniam, quis.</p>
    <p>Nam liber tempor cum soluta nobis eleifend option congue nihil imperdiet doming id quod mazim placerat facer possim assum. Typi non habent claritatem insitam; est usus legentis in iis qui facit eorum claritatem.</p>
  </div>
</section>

<!-- categories -->
<svg class="abs cards" style="top:244px" viewBox="0 0 470 125" aria-hidden="true">
  <path d="M12 0 H210 L265 62 L210 124 H12 Q2 124 2 112 V12 Q2 0 12 0Z" fill="var(--card)"/>
  <path d="M228 0 H456 Q468 0 468 12 V112 Q468 124 456 124 H228 L282 62Z" fill="var(--card)"/>
</svg>
<svg class="abs cards" style="top:424px" viewBox="0 0 470 125" aria-hidden="true">
  <path d="M12 0 H210 L265 62 L210 124 H12 Q2 124 2 112 V12 Q2 0 12 0Z" fill="var(--card)"/>
  <path d="M228 0 H456 Q468 0 468 12 V112 Q468 124 456 124 H228 L282 62Z" fill="var(--card)"/>
</svg>

<div class="abs badge" role="img" aria-label="Star category emblem" style="left:596px;top:232px;background:radial-gradient(circle,#f9c12a,#e78a12)"></div>
<h3 class="abs cat-title" style="left:673px;top:262px;color:var(--star)">STAR</h3>
<p class="abs cat-text" style="left:602px;top:304px">Lorem ipsum dolor sit amet, con-sectetur adipisicing elit, sed do eiusmod tempor incididunt ut labore et dolore magna... <span class="more">more</span></p>

<div class="abs badge" role="img" aria-label="Hero category emblem" style="left:846px;top:232px;background:radial-gradient(circle,#3d8cd0,#1d4f8e)"></div>
<h3 class="abs cat-title" style="left:924px;top:262px;color:var(--hero)">HERO</h3>
<p class="abs cat-text" style="left:860px;top:304px">Lorem ipsum dolor sit amet, con-sectetur adipisicing elit, sed do eiusmod tempor incididunt ut labore et dolore... <span class="more">more</span></p>

<div class="abs badge" role="img" aria-label="Leader category emblem" style="left:596px;top:412px;background:radial-gradient(circle,#8cbf3f,#3f6f1c)"></div>
<h3 class="abs cat-title" style="left:670px;top:442px;color:var(--leader)">LEADER</h3>
<p class="abs cat-text" style="left:602px;top:484px">Lorem ipsum dolor sit amet, con-sectetur adipisicing elit, sed do eiusmod tempor incididunt ut labore et dolore magna... <span class="more">more</span></p>

<div class="abs badge" role="img" aria-label="Icon category emblem" style="left:846px;top:412px;background:radial-gradient(circle,#f08ab0,#b81f63)"></div>
<h3 class="abs cat-title" style="left:920px;top:442px;color:var(--icon)">ICON</h3>
<p class="abs cat-text" style="left:860px;top:484px">Lorem ipsum dolor sit amet, con-sectetur adipisicing elit, sed do eiusmod tempor incididunt ut labore et dolore... <span class="more">more</span></p>

<!-- footer -->
<div class="abs rule" style="top:595px"></div>
<div class="abs win-badge" role="img" aria-label="Q-7 forum emblem"></div>
<h3 class="abs win-title">Q-7 the science of winning</h3>
<p class="abs win-text">Lorem ipsum dolor sit amet, consectetur adipisicing elit, sed do eius-mod tempor incididunt ut labore et dolore magna aliqua. Ut enim ad minim veniam, quis... <span class="more">more</span></p>

<span class="abs social" aria-label="Feed" style="left:787px;top:613px;background:#e8731c"></span>
<span class="abs social" aria-label="Social network" style="left:822px;top:613px;background:#2d8fc8"></span>
<span class="abs social" aria-label="Social network" style="left:787px;top:647px;background:#2d4f8e"></span>
<span class="abs social" aria-label="Social network" style="left:822px;top:647px;background:#3d7fb5"></span>

<ul class="abs foot-links">
  <li>Media</li>
  <li>Developers</li>
  <li>Terms &amp; Conditions</li>
  <li>Privacy Policy</li>
</ul>
<div class="abs rule" style="top:689px"></div>
<p class="abs copyright">© 2011 Zenthra.net</p>

</body>
</html>
```